International Life Insurer Needs a Web Design

What We Do: We are a boutique financial services firm specializing in solutions that financial services professionals can integrate into comprehensive wealth preservation strategies for their clients. Strategies we provide may run the spectrum from simple life insurance products to complex cases with very sophisticated and intricate solutions.

Industry Type: Financial & Insurance

Top Things to Communicate Through Our Web Design:
#1 Ultra High Net Worth
#2 INTERNATIONAL
#3 Private Banking
#4 Expertise
________________________________________
Our Target Audience:
Financial institutions/private banks who have high net worth/ultra high net worth international clients looking for unparalleled expertise in wealth preservation, taxation, and business insurance. The audience is the financial service professional, not the end client of the financial services. We will direct the professional to the site.
We Like These Designs. (fonts, colors, style):
Simple font, clean, modern, contemporary, blue colors
NOT stodgy, old, gothic, etc.

Secondarily, we’d like to also create a small tri-fold brochure incorporating the web elements (design, text), so the ability to transfer the design to print might be a plus.

Project Deadline Extended
Reason: to allow for additional design work

Target Market(s)

Financial services professionals catering to their ultra high net worth clients

Industry/Entity Type

Life Insurance

Requirements
Must have
• Our logo (see uploaded file)
Nice to have
• the existing website includes some text that could be reviewed for ideas and incorporated into the design: http://marlowcrestadvisory.example/

```html
<!DOCTYPE html>
<html lang="en">
<head>
<meta charset="utf-8">
<title>Marlowcrest Advisory Group</title>
<link href="https://fonts.googleapis.com/css2?family=PT+Sans+Narrow&family=Source+Sans+3:wght@400;600&display=swap" rel="stylesheet">
<style>
:root{
  --blue:#2f94c8;
  --blue-band:#3596c9;
  --accent:#1b8fd0;
  --navy:#0e3f7c;
  --footer:#1c4a7e;
  --footer-dark:#0e2745;
  --page:#eceef0;
  --header:#f4f5f6;
  --card:#ffffff;
  --text:#555b61;
  --heading:#3d4247;
  --rule:#cfd2d6;
}
*{margin:0;padding:0;box-sizing:border-box}
html,body{width:1200px;height:1200px;overflow:hidden}
body{position:relative;background:var(--page);font-family:"Source Sans 3",sans-serif;color:var(--text)}
.abs{position:absolute}
.top-stripe{left:0;top:0;width:1200px;height:7px;background:var(--blue)}
.site-header{left:0;top:7px;width:1200px;height:94px;background:var(--header)}
.brand{left:180px;top:28px;display:flex;align-items:center;gap:10px}
.brand-mark{width:22px;height:22px;background:var(--navy)}
.brand-name{font-size:28px;font-weight:400;color:var(--navy);line-height:1;letter-spacing:-.3px}
.main-nav{top:46px;left:590px;font-family:"PT Sans Narrow",sans-serif;font-size:15px;letter-spacing:1.6px;color:var(--heading)}
.main-nav span{position:absolute;white-space:nowrap}
.main-nav .active{color:var(--accent)}
.hero-band{left:0;top:101px;width:1200px;height:328px;background:var(--blue-band)}
.hero-frame{left:183px;top:115px;width:821px;height:301px;background:#a9d6ec;box-shadow:0 2px 6px rgba(0,0,0,.2)}
.hero-photo{left:190px;top:122px;width:807px;height:286px;background:linear-gradient(120deg,#6d7c8c 0%,#d9d3cc 45%,#f1ede8 60%,#46505c 100%)}
.title-row{display:flex;align-items:center;height:24px}
.section-title{font-family:"PT Sans Narrow",sans-serif;font-size:18px;font-weight:400;letter-spacing:1.3px;color:var(--heading);white-space:nowrap;line-height:24px}
.section-title em{font-style:normal;color:var(--accent)}
.title-rule{flex:1;height:11px;margin-left:12px;background:var(--rule)}
.card{background:var(--card)}
.intro-text{font-size:11px;line-height:20.6px;width:375px}
.dot{display:inline-block;width:8px;height:8px;border-radius:50%;background:var(--blue);margin-right:5px;vertical-align:-0.5px}
.btn{background:var(--navy);color:#fff;font-size:11px;font-weight:600;text-align:center;line-height:26px}
.thumb{height:100px}
.card-title{font-size:13px;font-weight:600;color:var(--heading)}
.card-text{font-size:11px;line-height:17.2px}
.link{color:var(--accent)}
.lower-text{font-size:11px;line-height:17.2px;width:235px}
.vrule{border-left:1px dotted #b9bec3}
.form-label{font-size:11px;color:var(--accent)}
.field{width:213px;height:25px;background:#eff0f1;border:1px solid #c8cbce;font-size:10.5px;font-style:italic;color:#444;padding-left:10px;line-height:23px}
.go{width:24px;height:24px;background:var(--navy);color:#fff;font-size:10px;font-weight:600;text-align:center;line-height:22px}
.site-footer{left:0;top:1075px;width:1200px;height:115px;background:var(--footer);color:#fff;font-size:10px}
.footer-base{left:0;top:1190px;width:1200px;height:10px;background:var(--footer-dark)}
.footer-links{text-align:right;line-height:20.6px}
</style>
</head>
<body>
<div class="abs top-stripe"></div>
<header class="abs site-header"></header>
<div class="abs brand"><span class="brand-mark"></span><span class="brand-name">Marlowcrest Advisory Group</span></div>
<nav class="abs main-nav">
  <span class="active" style="left:0">HOME</span>
  <span style="left:72px">ABOUT</span>
  <span style="left:150px">SOLUTIONS</span>
  <span style="left:252px">CASE SUDIES</span>
  <span style="left:361px">CONTACT</span>
</nav>

<div class="abs hero-band"></div>
<div class="abs hero-frame"></div>
<div class="abs hero-photo" role="img" aria-label="Business professionals shaking hands in a bright office"></div>

<div class="abs title-row" style="left:197px;top:447px;width:808px">
  <h2 class="section-title">SPECIALIZING IN COMPREHENSIVE <em>WEALTH PRESERVATION STRATEGIES FOR OUR CLIENTS</em></h2>
  <div class="title-rule"></div>
</div>

<section class="abs card" style="left:183px;top:485px;width:404px;height:210px"></section>
<p class="abs intro-text" style="left:200px;top:497px"><span class="dot"></span>SIn posuere ante in orci molestie adipiscing porta quam commodo. Sus-pendisse ut ligula nisi, cursus ullamcorper orci.<br>Nulla vulputate sodales metus, eget dignissim mi volutpat eu. Pellentesque nisi sem, euismod sit amet bibendum at, euismod a est. Morbi mattis bibendum sapien at ullamcorper.<br>Proin hendrerit, justo id hendrerit consectetur, lectus elit rhoncus eros, et adipi-scing felis quam at nibh. Maecenas tincidunt pretium lectus, at tempor arcu</p>
<div class="abs btn" style="left:200px;top:653px;width:87px">read more</div>

<article class="abs card" style="left:598px;top:485px;width:197px;height:210px"></article>
<div class="abs thumb" role="img" aria-label="Hands signing documents at a meeting table" style="left:598px;top:485px;width:197px;background:linear-gradient(135deg,#8b8f94,#e6e6e4 55%,#a7a9ab)"></div>
<h3 class="abs card-title" style="left:607px;top:593px">Image Headline One</h3>
<p class="abs card-text" style="left:608px;top:614px;width:180px">Cam sociis natoque penatibus et magnis dis parturient montes, nasce-tur ridiculus mus. Nunc a viverra turpis susepi &nbsp;<span class="link">read more &rarr;</span></p>

<article class="abs card" style="left:807px;top:485px;width:197px;height:210px"></article>
<div class="abs thumb" role="img" aria-label="Colleagues talking in a modern office with a laptop" style="left:807px;top:485px;width:197px;background:linear-gradient(135deg,#cfd6da,#f3f4f3 50%,#6f7478)"></div>
<h3 class="abs card-title" style="left:817px;top:593px">Image Headline Two</h3>
<p class="abs card-text" style="left:818px;top:614px;width:180px">Cam sociis natoque penatibus et magnis dis parturient montes, nasce-tur ridiculus mus. Nunc a viverra turpis susepi &nbsp;<span class="link">read more &rarr;</span></p>

<div class="abs title-row" style="left:198px;top:728px;width:527px">
  <h2 class="section-title">HEADLINE <em>TWO</em></h2>
  <div class="title-rule"></div>
</div>
<div class="abs title-row" style="left:749px;top:728px;width:255px">
  <h2 class="section-title">FIND OUT <em>MORE</em></h2>
  <div class="title-rule"></div>
</div>

<section class="abs card" style="left:183px;top:765px;width:542px;height:228px"></section>
<h3 class="abs card-title" style="left:200px;top:785px">Lower Headline One</h3>
<p class="abs lower-text" style="left:200px;top:817px"><span class="dot"></span>In posuere ante in orci molestie adipiscing porta quam commodo. Suspendisse ut ligula nisi, cursus ullamcorper orci. Nulla vulputate sodales metus, eget dignissim mi volutpat eu. Pellen-tesque nisi sem, euismod sit amet bibendum at, euismod a est. Morbi mattis bibendum sapien at ullamcorper. significant returns.</p>
<span class="abs link" style="left:206px;top:952px;font-size:12px">read more &rarr;</span>
<div class="abs vrule" style="left:454px;top:780px;height:198px"></div>
<h3 class="abs card-title" style="left:474px;top:785px">Lower Headline Two</h3>
<p class="abs lower-text" style="left:474px;top:817px"><span class="dot"></span>In posuere ante in orci molestie adipiscing porta quam commodo. Suspendisse ut ligula nisi, cursus ullamcorper orci.<br>Nulla vulputate sodales metus, eget dignissim mi volutpat eu. Pellentesque nisi sem, euismod sit amet bibendum at, euismod a est.<br>Morbi mattis bibendum sapien at ullamcorper.</p>
<span class="abs link" style="left:475px;top:952px;font-size:12px">read more &nbsp;&rarr;</span>

<section class="abs card" style="left:738px;top:765px;width:267px;height:228px"></section>
<p class="abs card-title" style="left:749px;top:784px;line-height:19px;width:220px">If you are interested in our service please fill in our form</p>
<label class="abs form-label" style="left:751px;top:828px">Your Name</label>
<div class="abs field" style="left:750px;top:847px">Enter your full name and title</div>
<label class="abs form-label" style="left:751px;top:882px">Business Name :</label>
<div class="abs field" style="left:750px;top:901px">Please enter name &amp; City branch</div>
<label class="abs form-label" style="left:751px;top:934px">Your Email :</label>
<div class="abs field" style="left:750px;top:953px">Please enter email address</div>
<div class="abs go" style="left:970px;top:954px">go</div>

<footer class="abs site-footer">
  <div class="abs" style="left:181px;top:18px;line-height:20.6px">© Copyright 2012 &nbsp;All rights reserved.<br>233 Street Blvd., Second Add.<br>City Name, &nbsp;123456<br>Tel: 0000 1234567</div>
  <div class="abs footer-links" style="right:312px;top:16px"><span style="color:#4bb0e6">Homepage</span><br>About Us<br>Solutions<br>Contact Us</div>
  <div class="abs footer-links" style="right:200px;top:18px">Case Studies<br>Disclaimer<br>Privacy Policy<br>Social Media</div>
</footer>
<div class="abs footer-base"></div>
</body>
</html>
```